Postcard Design

We are Brightmoor Care. A new way of providing quality healthcare for less. We offer a monthly membership program for $77 per person, $167 per family and cover about 85% of medical conditions. Medical office visits are just $7 each. This innovative program have already saved millions of dollars for it's members in health care costs. We are inviting people to a brief, educational meeting to learn more about how they can save money on their healthcare. We need something catchy and upbeat, positive with 1-2 photos inviting them to come find out more. We will be having appetizers. The date is Wednesday, Feb. 18 drop by between 6-8 pm
Industry/Entity Type
Healthcare

```html
<!DOCTYPE html>
<html lang="en">
<head>
<meta charset="utf-8">
<title>Brightmoor Care – Postcard</title>
<link rel="stylesheet" href="https://fonts.googleapis.com/css2?family=Open+Sans:wght@400;600;700;800&display=swap">
<style>
  :root {
    --blue: #1683b8;
    --blue-text: #1a7db3;
    --orange: #f6921e;
    --grey-panel: #e4e5e7;
    --grey-pill: #a3a5a8;
    --grey-text: #5a5c5f;
    --grey-head: #77797c;
    --sky: #dcedf8;
    --white: #ffffff;
    --page: #eef0f2;
  }
  * { box-sizing: border-box; margin: 0; padding: 0; }
  html, body { width: 788px; height: 1200px; overflow: hidden; }
  body {
    background: var(--page);
    font-family: "Open Sans", Arial, sans-serif;
    color: var(--grey-text);
    position: relative;
  }
  .postcard {
    position: absolute;
    left: 74px;
    width: 640px;
    height: 496px;
    overflow: hidden;
    box-shadow: 0 4px 12px rgba(0,0,0,.18);
  }
  .postcard--front {
    top: 56px;
    background: linear-gradient(160deg, var(--sky) 0%, #f3f6f8 35%, #eceef0 100%);
  }
  .postcard--back {
    top: 628px;
    background: linear-gradient(90deg, #f1f3f5 0%, #e9f3fa 60%, var(--sky) 100%);
  }
  .wave-layer { position: absolute; inset: 0; width: 640px; height: 496px; }
  .bottom-bar {
    position: absolute; left: 0; right: 0; bottom: 0; height: 21px;
    background: var(--blue);
  }
  .headline {
    position: absolute;
    font-weight: 700;
    font-size: 23px;
    letter-spacing: -0.2px;
    text-transform: uppercase;
  }
  .postcard--front .headline { left: 33px; top: 46px; color: var(--blue-text); }
  .postcard--back .headline { left: 186px; top: 112px; color: var(--grey-head); }

  .brand {
    position: absolute;
    display: flex; align-items: center; gap: 7px;
    color: var(--blue-text);
    font-weight: 700;
    font-size: 20px;
    white-space: nowrap;
  }
  .brand__dot {
    width: 14px; height: 14px; border-radius: 50%;
    background: var(--orange); flex: none;
  }
  .postcard--front .brand { right: 26px; top: 52px; }
  .postcard--back .brand { left: 22px; top: 64px; }

  .photo {
    position: absolute;
  }
  .photo--couple {
    left: 0; top: 140px; width: 408px; height: 335px;
    background: radial-gradient(ellipse at 45% 45%, #f2d2bc 0%, #e7c2a6 35%, #f4f1ee 70%, #ffffff 100%);
  }
  .photo--coins {
    left: 0; top: 394px; width: 271px; height: 81px;
    background: linear-gradient(90deg, #e9eadf 0%, #d8d9cc 40%, #c9cabd 60%, #e6e6dd 100%);
  }

  .membership {
    position: absolute; left: 408px; top: 204px; width: 232px; height: 271px;
    background: var(--grey-panel);
    padding: 0 14px 0 12px;
  }
  .membership__pill {
    position: absolute; left: 12px; top: -6px; width: 210px; height: 30px;
    background: var(--grey-pill);
    border: 2px solid var(--white);
    border-radius: 8px;
    color: var(--white);
    font-size: 13px;
    line-height: 26px;
    text-align: center;
  }
  .membership__list {
    list-style: none;
    margin-top: 39px;
    padding-left: 24px;
  }
  .membership__list li {
    position: relative;
    font-size: 14px;
    line-height: 17px;
    margin-bottom: 8px;
    padding-left: 18px;
  }
  .membership__list svg {
    position: absolute; left: -4px; top: 2px; width: 14px; height: 14px;
  }
  .membership__visits {
    font-size: 13px;
    margin-top: 6px;
    letter-spacing: -0.2px;
  }
  .membership__visits strong { font-weight: 700; }
  .membership__invite {
    margin-top: 22px;
    color: var(--blue-text);
    font-size: 13.5px;
    line-height: 19px;
    text-align: center;
  }

  .event {
    position: absolute; left: 0; top: 165px; width: 271px; height: 229px;
    background: var(--grey-panel);
    padding: 12px 14px 0 28px;
  }
  .event__intro {
    font-size: 14px; line-height: 18px; margin-bottom: 6px;
  }
  .event__name {
    margin-top: 8px;
    color: var(--blue-text);
    font-weight: 700;
    font-size: 23px;
    text-align: center;
    line-height: 28px;
  }
  .event__invite {
    color: #111;
    font-weight: 700;
    font-size: 17px;
    text-align: center;
    margin-top: 4px;
  }
  .event__when {
    color: var(--grey-head);
    font-weight: 700;
    font-size: 14px;
    line-height: 18px;
    text-align: center;
    margin-top: 2px;
  }
</style>
</head>
<body>

<!-- Front of postcard -->
<section class="postcard postcard--front">
  <div class="photo photo--couple" role="img" aria-label="Photo of a smiling older couple embracing"></div>

  <svg class="wave-layer" viewBox="0 0 640 496" aria-hidden="true">
    <path fill="#eef2f5" d="M0 0 H640 V160 C560 190 480 160 400 150 C260 120 120 150 0 175 Z"/>
    <path fill="var(--blue)" d="M0 135 C150 100 300 105 420 150 C500 180 580 175 640 150 L640 210 C570 220 480 200 400 180 C280 150 140 150 0 195 Z"/>
    <path fill="var(--white)" d="M0 195 C140 150 280 150 400 180 C480 200 570 220 640 210 L640 216 C570 226 480 206 400 186 C280 156 140 158 0 200 Z"/>
    <path fill="var(--orange)" d="M300 128 C420 145 560 115 640 78 L640 96 C560 135 420 158 300 128 Z"/>
  </svg>

  <h1 class="headline">Quality Healthcare for Less!</h1>
  <div class="brand"><span class="brand__dot"></span>Brightmoor Care</div>

  <aside class="membership">
    <div class="membership__pill">Monthly Membership Program</div>
    <ul class="membership__list">
      <li><svg viewBox="0 0 14 14"><circle cx="7" cy="7" r="7" fill="var(--orange)"/><path d="M5.5 4 L8.5 7 L5.5 10" stroke="#fff" stroke-width="1.8" fill="none"/></svg>$77 per person</li>
      <li><svg viewBox="0 0 14 14"><circle cx="7" cy="7" r="7" fill="var(--orange)"/><path d="M5.5 4 L8.5 7 L5.5 10" stroke="#fff" stroke-width="1.8" fill="none"/></svg>$167 per family</li>
      <li><svg viewBox="0 0 14 14"><circle cx="7" cy="7" r="7" fill="var(--orange)"/><path d="M5.5 4 L8.5 7 L5.5 10" stroke="#fff" stroke-width="1.8" fill="none"/></svg>cover about 85% of medical conditions</li>
    </ul>
    <p class="membership__visits">Medical office visits are just <strong>$7</strong> each</p>
    <p class="membership__invite">We are inviting you to a brief, educational meeting to learn more about how you can save money on your healthcare.</p>
  </aside>

  <div class="bottom-bar"></div>
</section>

<!-- Back of postcard -->
<section class="postcard postcard--back">
  <svg class="wave-layer" viewBox="0 0 640 496" aria-hidden="true">
    <path fill="var(--blue)" d="M0 0 H640 V62 C560 50 460 48 380 58 C250 75 120 70 0 45 Z"/>
    <path fill="var(--orange)" d="M195 88 C330 62 500 50 640 68 L640 82 C500 66 330 75 195 88 Z"/>
  </svg>

  <div class="brand"><span class="brand__dot"></span>Brightmoor Care</div>
  <h2 class="headline">Quality Healthcare for Less!</h2>

  <div class="event">
    <p class="event__intro">A new way of providing quality healthcare for less.</p>
    <p class="event__intro">This innovative program have already saved millions of dollars for it's members in health care costs.</p>
    <p class="event__name">Brightmoor Care</p>
    <p class="event__invite">Inviting You</p>
    <p class="event__when">Wednesday, Feb. 18<br>between 6-8 pm</p>
  </div>

  <div class="photo photo--coins" role="img" aria-label="Photo of a stack of coins resting on banknotes"></div>

  <div class="bottom-bar"></div>
</section>

</body>
</html>
```